Flyer for International Internship Program in Dublin, Ireland

We need a one-page flyer promoting our newest internship program in Dublin, Ireland called "Venture Lantern". Northbound Placements provides international internship programs (like a study abroad) for university students. The Venture Lantern program is 10 weeks and includes full-time internship in an Irish start-up company, panel discussions with entrepreneurs and industry leaders, and a business competition along with social events and housing in Dublin. The flyer must convey the purpose of the program to university students as well as be fun and professional.
Updates

I've posted a new logo in .png format. Please let me know if there are any issues with that file. 

We've made some changes to text:

1. Please change the title to: 
Venture Lantern 
Dublin Entrepreneur Internship Program 

2. Please add the price: $7,190
3. Please add an Irish and American flag 
4. Please be sure that the color scheme is similar to that palette of the logo

Target Market(s)

We are trying to attract university students (21-23) as well as college staff like study abroad offices and advisors.

Industry/Entity Type

University

Requirements
Must have
• We would like to see flyers convey all of the content attached as well as images of Dublin, and business/professional themed photos. The flyer must have our logo (attached) and website. We'd like the information divided into sections so it looks clean and easy to read.
Nice to have
• We'd like to see some color (like our logo), but it doesn't need to be too bright or overwhelming. Young, but professional.
Should not have
• Do not use any overly styled fonts like scripts or "Celtic-looking" text.

```html
<!DOCTYPE html>
<html lang="en">
<head>
<meta charset="utf-8">
<title>Venture Lantern — Dublin Entrepreneur Internship Program</title>
<link rel="stylesheet" href="https://fonts.googleapis.com/css2?family=Tinos:wght@400;700&family=Arimo:wght@700&display=swap">
<style>
  :root {
    --ink: #1c1c1c;
    --navy: #2d4d68;
    --steel: #4b86ab;
    --ribbon-dark: #2f6d97;
    --sky: #88bfdc;
    --olive: #8d9a2b;
    --white: #ffffff;
    --rule: #c9c9c9;
  }
  * { box-sizing: border-box; margin: 0; padding: 0; }
  html, body { width: 926px; height: 1200px; overflow: hidden; background: var(--white); }
  body { position: relative; font-family: "Tinos", "Times New Roman", serif; color: var(--ink); }

  .brand { position: absolute; left: 84px; top: 52px; display: flex; align-items: center; gap: 16px; }
  .brand-dot { width: 64px; height: 64px; border-radius: 50%; background: var(--steel); }
  .brand-name { font-family: "Tinos", serif; font-weight: 700; font-size: 27px; line-height: 1.05; color: var(--navy); width: 200px; }

  .header-rule { position: absolute; left: 404px; top: 0; width: 3px; height: 146px; background: var(--olive); }
  .flags { position: absolute; left: 428px; top: 30px; display: flex; gap: 14px; }
  .program { position: absolute; left: 428px; top: 68px; }
  .program-title { font-weight: 400; font-size: 35px; letter-spacing: 0.5px; color: var(--navy); text-transform: uppercase; line-height: 1; }
  .program-subtitle { font-size: 23px; color: var(--olive); margin-top: 6px; line-height: 1.1; }
  .program-dates { font-size: 18px; font-weight: 700; color: var(--ink); margin-top: 6px; }

  .photo-strip { position: absolute; top: 178px; left: 0; width: 926px; height: 258px; }
  .photo { position: absolute; top: 0; height: 258px; }
  .photo-castle { left: 0; width: 292px; background: linear-gradient(180deg, #b9b7b0 0%, #8f8c84 55%, #4e6b3a 80%, #b8322a 100%); }
  .photo-office { left: 298px; width: 368px; background: linear-gradient(135deg, #b7c2c9 0%, #5f6b74 45%, #2b2f35 100%); }
  .photo-bridge { left: 672px; width: 254px; background: linear-gradient(180deg, #334d78 0%, #4d6390 45%, #c9a35a 70%, #2a2f44 100%); }

  .section-rule { position: absolute; top: 501px; height: 1px; background: var(--rule); }
  .ribbon { position: absolute; top: 481px; height: 41px; background: var(--steel); color: var(--white);
    font-family: "Arimo", Arial, sans-serif; font-weight: 700; font-size: 25px; line-height: 41px; text-align: center;
    clip-path: polygon(0 0, 100% 0, 95% 50%, 100% 100%, 0 100%, 5% 50%); }
  .ribbon-why { left: 144px; width: 257px; }
  .ribbon-experience { left: 522px; width: 250px; }

  .copy { position: absolute; top: 548px; font-size: 16px; line-height: 23px; }
  .copy-why { left: 91px; width: 335px; }
  .copy-experience { left: 463px; width: 370px; }
  .copy-divider { position: absolute; left: 461px; top: 548px; width: 1px; height: 152px; background: var(--rule); }

  .inclusions { position: absolute; left: 91px; top: 731px; width: 741px; height: 320px; background: var(--sky); overflow: visible; }
  .inclusions-ribbon { position: absolute; left: -42px; top: 36px; width: 210px; height: 42px; background: var(--ribbon-dark); color: var(--white);
    font-family: "Arimo", Arial, sans-serif; font-weight: 700; font-size: 25px; line-height: 42px; text-align: center;
    transform: rotate(-45deg); }
  .inclusion-list { position: absolute; left: 130px; top: 22px; width: 400px; list-style: none; }
  .inclusion-list li { position: relative; padding-left: 22px; font-size: 15px; line-height: 18px; margin-bottom: 10px; }
  .inclusion-list li:last-child { margin-bottom: 0; }
  .inclusion-list li::before { content: "+"; position: absolute; left: 2px; top: 0; color: var(--white); font-family: "Arimo", sans-serif; font-weight: 700; }
  .inclusions-divider { position: absolute; left: 560px; top: 28px; width: 2px; height: 264px; background: var(--white); }
  .inclusion-icons { position: absolute; left: 600px; top: 50px; }

  .footer-rule { position: absolute; top: 1055px; width: 3px; height: 145px; background: var(--olive); }
  .footer-rule-a { left: 386px; }
  .footer-rule-b { left: 545px; }
  .apply { position: absolute; left: 106px; top: 1064px; }
  .apply-title { font-weight: 700; font-size: 42px; color: var(--olive); line-height: 1; }
  .apply-web { font-weight: 700; font-size: 17px; margin-top: 8px; }
  .fee { position: absolute; left: 398px; top: 1070px; width: 140px; text-align: center; }
  .fee-label { font-weight: 700; font-size: 15px; }
  .fee-amount { font-weight: 700; font-size: 44px; color: var(--olive); line-height: 1.1; margin-top: 4px; }
  .contact { position: absolute; left: 567px; top: 1068px; }
  .contact-email { font-weight: 700; font-size: 18px; }
  .contact-phone { font-weight: 700; font-size: 35px; line-height: 1.1; margin-top: 6px; }
</style>
</head>
<body>

<div class="brand">
  <span class="brand-dot"></span>
  <span class="brand-name">Northbound Placements</span>
</div>

<div class="header-rule"></div>

<div class="flags">
  <svg width="52" height="30" viewBox="0 0 52 30" aria-label="American flag">
    <rect width="52" height="30" fill="#ffffff"/>
    <g fill="#b22234">
      <rect y="0" width="52" height="2.3"/><rect y="4.6" width="52" height="2.3"/><rect y="9.2" width="52" height="2.3"/>
      <rect y="13.8" width="52" height="2.3"/><rect y="18.4" width="52" height="2.3"/><rect y="23" width="52" height="2.3"/>
      <rect y="27.6" width="52" height="2.4"/>
    </g>
    <rect width="22" height="16" fill="#3c3b6e"/>
  </svg>
  <svg width="48" height="30" viewBox="0 0 48 30" aria-label="Irish flag">
    <rect width="16" height="30" fill="#169b62"/>
    <rect x="16" width="16" height="30" fill="#ffffff"/>
    <rect x="32" width="16" height="30" fill="#ff883e"/>
  </svg>
</div>

<div class="program">
  <h1 class="program-title">Venture Lantern</h1>
  <p class="program-subtitle">Dublin Entrepreneur Internship Program</p>
  <p class="program-dates">May 31 - August 9, 2014</p>
</div>

<div class="photo-strip">
  <div class="photo photo-castle" role="img" aria-label="Photo of a Dublin stone castle archway with red tulips in the foreground"></div>
  <div class="photo photo-office" role="img" aria-label="Photo of three young professionals reviewing documents at a laptop in an office"></div>
  <div class="photo photo-bridge" role="img" aria-label="Photo of a lit footbridge over the River Liffey at dusk"></div>
</div>

<div class="section-rule" style="left:91px;width:363px"></div>
<div class="section-rule" style="left:478px;width:354px"></div>
<div class="ribbon ribbon-why">Why Dublin?</div>
<div class="ribbon ribbon-experience">The Experience</div>

<p class="copy copy-why">Dublin is at the heart of new European investment in business innovation and we can’t imagine a better place to launch your career. As the European headquarters for many of the leading tech and social media corporations, the city is gaining traction as a dynamic place to create and grow business.</p>
<div class="copy-divider"></div>
<p class="copy copy-experience">Northbound Placements wants to help young professionals embrace Dublin’s entrepreneurship. Along with a full-time internship in Irish start-ups, interns will tour companies like Keystone Systems, have discussions with industry leaders and partake in a business competition complete with prizes.</p>

<section class="inclusions">
  <div class="inclusions-ribbon">Inclusions</div>
  <ul class="inclusion-list">
    <li>Centralized housing in Liffey Collegiate Hall.</li>
    <li>Guaranteed internship withing a startup or<br>entrepreneurial enterprise.</li>
    <li>Panel Discussions.</li>
    <li>Site visits with companies including Keystone Systems.</li>
    <li>Networking events.</li>
    <li>Entrepreneurship challenge with prizes.</li>
    <li>Social events and excursions.</li>
    <li>24/7 on the ground staff support.</li>
    <li>Career development and access to the Clearpath Strengths<br>Profile assessment.</li>
  </ul>
  <div class="inclusions-divider"></div>
  <svg class="inclusion-icons" width="110" height="220" viewBox="0 0 110 220" fill="none" stroke="#ffffff" stroke-width="3">
    <circle cx="30" cy="30" r="22" fill="#ffffff" stroke="none"/>
    <path d="M52 36 C 80 45, 85 70, 70 82" stroke-dasharray="4 4" stroke-width="2"/>
    <rect x="35" y="88" width="56" height="38" rx="3" fill="#ffffff" stroke="none"/>
    <rect x="55" y="126" width="16" height="8" fill="#ffffff" stroke="none"/>
    <path d="M40 136 C 20 150, 20 165, 32 175" stroke-dasharray="4 4" stroke-width="2"/>
    <path d="M38 180 L62 160 L70 168 L46 188 Z" fill="#ffffff" stroke="none"/>
    <path d="M38 180 L34 194 L46 188 Z" fill="#ffffff" stroke="none"/>
  </svg>
</section>

<div class="footer-rule footer-rule-a"></div>
<div class="footer-rule footer-rule-b"></div>

<div class="apply">
  <p class="apply-title">APPLY NOW</p>
  <p class="apply-web">www.northboundplacements.com</p>
</div>

<div class="fee">
  <p class="fee-label">Registration Fee</p>
  <p class="fee-amount">$7,190</p>
</div>

<div class="contact">
  <p class="contact-email">info@northboundplacements.com</p>
  <p class="contact-phone">1-410-555-0143</p>
</div>

</body>
</html>
```